Corporate Personal Training Business needs a flyer for High Scale apartment complex contract

We are looking at getting a flyer for a high scale apartment complex that will explain the prices and services on the back page and offer a complimentary personal training session on the front page as well as a welcome and so on. I will attach plenty of information and also a copy of a basic flyer that does not look very good but will give you an understanding of what I am looking at doing.

Attached I will include all required information as well as pictures I wish to be used in the flyer also and any other information I can think of adding.

Logo design is already done but I am open to suggestion for new logos if you would like to make that part of the project.

The opening day for this project is on Sunday the 14th of July so I do not have a massive amount of time but more then enough to get the project done.

All required pictures can be accessed via the files I have uploaded.

Please note that 72 Marlow logo needs to be the same as the file I have attached.
Updates

PDF Format of the flyer has been uploaded here you can find logos, photos and information that is required.

All info on the flyer needs to be included just needs to look much more professional. Thankyou

Target Market(s)

Upmarket business people for the most part might have a few young people but generally 35+

Industry/Entity Type

Apartment

Requirements
Must have
• From page one you will see various pictures displaying the types of training I can provide. Kettlebells weights kickboxing etc. These pictures are required unless you feel they will be placed in written form somewhere to make it look better. I liked the idea of making that visual but it is up to you.

The flyer must be 1 page front and back with the front being very attractive to the eye and outlining the complimentary PT session. The info displayed on the front page can be shortened down if necessary as long as the basic idea is projected across and people are aware that the services provided have a wide variety and are fun.

I want the photo of the trainer included as well as the logo above info is also required such as ABN number business name obviously and so on.

Also There needs to be mention that the Owners Corporation will be covering cost of the induction until Jan 2014

Should not have
• A different font with 72 Marlow the attached image on the flyer is what needs to be used as its the 72 marlow logo

```html
<!DOCTYPE html>
<html lang="en">
<head>
<meta charset="utf-8">
<title>Bright Path Wellness – Corporate Personal Training Flyer</title>
<link href="https://fonts.googleapis.com/css2?family=PT+Sans:wght@400;700&family=PT+Sans+Narrow:wght@400;700&display=swap" rel="stylesheet">
<style>
  :root{
    --page-bg:#e4e6e9;
    --paper:#ffffff;
    --blue-deep:#0654a6;
    --blue-mid:#1479c8;
    --blue-light:#5fb4ea;
    --blue-pale:#d6eefb;
    --ink:#1c2a3a;
    --navy:#0b2f52;
    --teal:#1f7f86;
    --white:#ffffff;
  }
  *{box-sizing:border-box;margin:0;padding:0}
  html,body{width:1186px;height:1200px;overflow:hidden;background:var(--page-bg)}
  body{position:relative;font-family:"PT Sans",Arial,sans-serif}

  .flyer{position:absolute;left:179px;top:65px;width:830px;height:1070px;background:var(--paper);padding:17px}
  .sheet{position:relative;width:796px;height:1036px;overflow:hidden;
    background:
      radial-gradient(ellipse 420px 200px at 470px 760px, rgba(120,200,245,.75), transparent 70%),
      radial-gradient(ellipse 300px 260px at 700px 330px, rgba(90,170,230,.55), transparent 70%),
      linear-gradient(180deg, #2f86c9 0%, #1c74c0 25%, #0c5fae 55%, #1677c6 75%, #0a58a8 100%);}

  .business{position:absolute;left:38px;top:30px;color:var(--white);line-height:30px}
  .business__name{font-weight:700;font-size:25px;letter-spacing:.2px}
  .business__line{font-size:22px}

  .brand-mark{position:absolute;left:458px;top:8px;color:var(--white);font-weight:700;font-size:72px;line-height:80px}
  .brand-panel{position:absolute;left:535px;top:92px;width:261px;height:170px;background:var(--white);
    display:flex;flex-direction:column;align-items:center;justify-content:center;gap:10px}
  .brand-panel__name{color:var(--teal);font-size:26px;font-weight:400}
  .brand-panel__square{width:40px;height:40px;border:3px solid var(--blue-light)}

  .trainer-photo{position:absolute;left:0;top:158px;width:178px;height:200px;
    background:linear-gradient(160deg,#4c5660 0%,#1d2329 60%,#0c0f12 100%)}
  .partner-tag{position:absolute;left:0;top:358px;width:178px;height:92px;background:#d9dde1;
    display:flex;align-items:center;justify-content:center;color:#111;font-size:34px;font-weight:700}

  .about{position:absolute;left:198px;top:166px;color:var(--navy)}
  .about__label{font-size:29px}
  .about__name{font-size:42px;margin-top:2px}

  .credentials{position:absolute;left:200px;top:268px;list-style:none;color:var(--white);
    font-family:"PT Sans Narrow",Arial,sans-serif;font-size:18px}
  .credentials li{display:flex;align-items:center;height:30px;white-space:nowrap}
  .credentials li::before{content:"";width:16px;height:16px;border-radius:50%;background:var(--white);margin-right:9px;flex:none}
  .credentials .big{font-size:28px;margin-left:6px}
  .credentials .small{font-size:14px;margin-left:5px}

  .info-box{position:absolute;left:17px;width:761px;padding:10px 14px;border-radius:3px;
    font-family:"PT Sans Narrow",Arial,sans-serif;font-size:15px;line-height:21px;color:var(--ink)}
  .info-box--1{top:462px;height:62px;background:rgba(230,246,255,.95)}
  .info-box--2{top:531px;height:63px;background:rgba(190,225,246,.85)}
  .info-box--3{top:600px;height:63px;background:rgba(190,225,246,.85)}

  .offer{position:absolute;left:33px;top:678px;width:740px;color:var(--white);font-size:31px;line-height:39px;
    text-shadow:-1px -1px 0 #0b3050,1px -1px 0 #0b3050,-1px 1px 0 #0b3050,1px 1px 0 #0b3050,2px 3px 3px rgba(0,0,0,.45)}

  .training-photo{position:absolute}
  .training-photo--boxing{left:0;top:816px;width:119px;height:79px;background:linear-gradient(120deg,#e9e3dc,#c94a3a)}
  .training-photo--core{left:103px;top:895px;width:120px;height:80px;background:linear-gradient(90deg,#d9a58c,#b57d62,#e0e0e0)}
  .training-photo--ball{left:223px;top:966px;width:104px;height:70px;background:linear-gradient(135deg,#ffffff,#c86fc0)}

  .partner-logo{position:absolute;left:238px;top:872px;width:180px;text-align:center;color:#0d0d0d;font-size:36px;font-weight:700}

  .contact{position:absolute;left:455px;top:846px;color:var(--white)}
  .contact__lead{font-size:21px;line-height:28px}
  .contact__phone{font-weight:700;font-size:34px;margin-top:10px;display:flex;align-items:center;gap:10px}
  .contact__web{position:absolute;left:455px;top:1000px;color:var(--white);font-size:16px}
</style>
</head>
<body>
  <div class="flyer">
    <div class="sheet">
      <header class="business">
        <div class="business__name">BRIGHT PATH WELLNESS</div>
        <div class="business__line">Corporate Personal Training</div>
        <div class="business__line">ABN: 12 345 678 901</div>
      </header>

      <div class="brand-mark">BPW</div>
      <div class="brand-panel">
        <span class="brand-panel__name">Bright Path</span>
        <span class="brand-panel__square"></span>
      </div>

      <div class="trainer-photo" role="img" aria-label="Portrait photo of the personal trainer"></div>
      <div class="partner-tag">72 Marlow</div>

      <section class="about">
        <div class="about__label">About the Trainer :</div>
        <div class="about__name">Daniel Hartley</div>
      </section>

      <ul class="credentials">
        <li>Passion For the Fitness Industry for over <span class="big">9 years</span></li>
        <li>6 years Taekwondo 2nd degree Black Belt</li>
        <li>3 Years Qualified Personal Trainer</li>
        <li>2 year Boot Camp Instructor</li>
        <li>Studied Kick Boxing, Muay Thai Boxing, Brazilian Jiu Jitsu Martial Arts <span class="small">(totalling over 4 years)</span></li>
        <li>Qualified Advanced Sports Nutrition Course</li>
      </ul>

      <p class="info-box info-box--1">72 Marlow and Bright Path Wellness have joined together to provide you with the convenience of one on one personal training within the privacy and comfort of your apartment complex in the Health &amp; Wellbeing Retreat .</p>
      <p class="info-box info-box--2">Whether your goal is to lose weight, tone up, increase fitness or to feel great for Summer we have a fitness expert who has helped hundreds of people just like you reach their health and fitness goals.</p>
      <p class="info-box info-box--3">More importantly, we will train your way using a variety of training styles including weights, kettle bells, full body strength and cardio, boxing and martial arts training keeping you interested and looking forward to your training sessions.</p>

      <p class="offer">Take Advantage of a Complimentary One on One Personal Training Session now by simply contacting Daniel Hartley and organizing a convenient time</p>

      <div class="training-photo training-photo--boxing" role="img" aria-label="Photo of boxing training with gloves"></div>
      <div class="training-photo training-photo--core" role="img" aria-label="Photo of toned midsections"></div>
      <div class="training-photo training-photo--ball" role="img" aria-label="Photo of an exercise ball workout"></div>

      <div class="partner-logo">72 Marlow</div>

      <section class="contact">
        <div class="contact__lead">For General &amp; Booking Enquires<br>Contact Daniel Hartley</div>
        <div class="contact__phone">0400 555 218</div>
      </section>
      <div class="contact__web">www.brightpathwellness.com.au</div>
    </div>
  </div>
</body>
</html>
```